Residential Mortgage Leader needs Wordpress Design

Looking for a home page website design for a client. We develop using the WordPress platform and would prefer the design be at least loosely based on an existing WordPress template. Attached files have many notes from our creative brief with client. The site must be responsive. Approved, basic wireframe attached. There is room for interpretation.

Existing web site: http://www.marisolbrandt.example/

The Marisol Brandt Team relies on strong systems to deliver an on-time, done-right, friendly experience. Marisol offers mortgages and refinancing services throughout the United States. She is a successful Keystone Funding agent who strives to be an active part of her community. She would like to focus the site on her team, rather than just her.

Difference makers...
When you work with the Marisol Brandt team you get a high level of expertise and a friendly experience.

She has amazing credentials. Marisol is widely recognized as a top producer for her company, and has earned a number of awards and honors for her customer service.

Marisol's team is very engaged and enjoys sharing social comments or photos from their community.

Imagery:
* Friendly, warm imagery, preferably of her team or an image to represent her team
* Clean and crisp
* Professional / Experts in mortgage and refinance
* Clean / Good use of white space
Updates

When possible, please use imagery from the DFW area. The client mentioned they would prefer not to see stock images. Thanks.

Amend that- creative use of stock images, however, is fine. A few designs have used stock imagery, but in a well-considered manner.

We added some photos and graphics that are local. We are Dallas / Ft. Worth, Plano, Frisco, Texas. We also added some examples of photos to use for the "In the Community" area. Stock photos of business folks just doesn't fit there. Thanks!

Target Market(s)

They service a lot of builders, but also work with homeowners. Their typical client is usually a woman searching for mortgage services online. She typically has a family and may refer her husband to Marisol's team. Keep in mind, however, they also see a number of other scenarios. Most of their clients are middle to high-end borrowers.

Industry/Entity Type

It Company

Requirements
Must have
• Design should be developed using program such as Photoshop or Fireworks or Illustrator as last preference. Ideally, the design would be based on an existing responsive WordPress theme, which we would customize. You must include the name of the target theme. The footer should include lots of space for disclaimers and legal language. Site navigation should include these choices: "Home, About, Builders, Mortgage Info, Approval, Blog, Contact"
Nice to have
• Blog, social media and photos area. Use of the already approved style prototype with colors and fonts (Lato- a Google font, Times New Roman and Cookie-a decorative Google font). However, we are open to interpretation.
Should not have
• Hard to read fonts or a lack of white space.

```html
<!DOCTYPE html>
<html lang="en">
<head>
<meta charset="utf-8">
<title>Keystone Funding – Marisol Brandt Team</title>
<link rel="stylesheet" href="https://fonts.googleapis.com/css2?family=Lato:ital,wght@0,400;0,700;1,400&display=swap">
<style>
:root{
  --dark:#2c2f31;
  --footer:#393a3b;
  --footer-bottom:#303132;
  --red:#c8361f;
  --orange:#d8661c;
  --ink:#2e2e2e;
  --body:#555;
  --muted:#9a9a9a;
  --link:#2a9bc4;
  --band:#56585a;
  --card:#f4f4f4;
  --line:#d6d6d6;
}
*{box-sizing:border-box;margin:0;padding:0}
html,body{width:847px;height:1200px;overflow:hidden}
body{position:relative;font-family:"Lato",sans-serif;color:var(--ink);background:#fff}
.abs{position:absolute}
.topbar{left:0;top:0;width:847px;height:112px;background:var(--dark)}
.topbar .rule{left:85px;top:38px;width:680px;height:1px;background:#3d4143}
.email{left:96px;top:12px;font-size:9px;color:#b9bcbe;display:flex;align-items:center;gap:8px}
.email svg{width:11px;height:9px}
.social-top{left:600px;top:12px;display:flex;gap:23px}
.social-top span{width:11px;height:11px;border-radius:50%;background:#6b6f72;display:block}
.brand{left:90px;top:67px;color:#fff}
.brand .name{font-size:17px;font-weight:700;color:#fff;display:flex;align-items:center;gap:6px}
.brand .name i{width:12px;height:12px;background:var(--red);display:block}
.brand .sub{font-size:7.5px;color:#e6e6e6;margin-top:2px;font-weight:700}
.nav{left:313px;top:71px;display:flex;height:41px;font-size:10px;color:#fff}
.nav a{color:#fff;text-decoration:none;display:flex;align-items:center;padding:0 15.5px}
.nav a.active{background:var(--red);padding:0 14px}
.hero{left:0;top:112px;width:847px;height:390px;background:linear-gradient(90deg,#b3a89a 0%,#9a9080 25%,#8a8d74 45%,#c9b39a 65%,#a8a08c 85%,#cfc3b0 100%)}
.hero .lawn{left:0;top:230px;width:847px;height:160px;background:linear-gradient(180deg,rgba(82,125,40,.6),rgba(60,110,30,.85))}
.hero-box{left:85px;top:265px;width:290px;height:104px;background:rgba(255,255,255,.9);padding:15px 14px}
.hero-box h1{font-weight:400;font-size:25px;color:#222;letter-spacing:.2px}
.hero-box p{font-size:10px;line-height:15px;color:#444;margin-top:10px}
.cta{left:85px;top:369px;display:flex;align-items:center;font-size:9.5px}
.btn{height:24px;display:flex;align-items:center;padding:0 10px;color:#fff}
.btn.red{background:var(--red)}
.btn.dark{background:#2d2f30}
.cta .or{color:#fff;padding:0 8px;font-size:10px}
.section-title{left:0;width:847px;text-align:center;font-size:18px;color:#333;font-weight:400}
.card{top:565px;width:333px;height:144px;border:1px solid var(--line);background:var(--card)}
.card .band{height:38px;background:var(--band);display:flex;align-items:center}
.card .icon{width:46px;height:38px;background:var(--red);position:relative;display:flex;align-items:center;justify-content:center}
.card .icon::after{content:"";position:absolute;right:-7px;top:13px;border-left:7px solid var(--red);border-top:6px solid transparent;border-bottom:6px solid transparent}
.card h3{color:#fff;font-size:15px;font-weight:700;margin-left:20px}
.card p{font-size:9.3px;line-height:15.6px;color:var(--body);padding:12px 9px 0 10px}
.col-label{top:785px;font-size:12px;color:#333}
.blog-icon{left:85px;top:822px;width:35px;height:35px;background:var(--orange);display:flex;align-items:center;justify-content:center}
.blog-date{left:85px;top:862px;width:35px;text-align:center;font-style:italic;color:#444}
.blog-date b{display:block;font-size:17px;font-weight:400}
.blog-date small{font-size:7px}
.blog-post{left:142px;top:827px;width:160px}
.blog-post h4{font-size:9.5px;font-weight:700;color:#333;line-height:13px}
.blog-post p{font-size:9px;line-height:13.5px;color:#8a8a8a;margin-top:10px}
.blog-post a{display:block;font-size:9.5px;color:#333;margin-top:10px;text-decoration:none}
.dotted{height:3px;background:repeating-linear-gradient(90deg,#cfcfcf 0 2px,transparent 2px 4px)}
.tweet{left:323px;width:200px;display:flex;gap:18px}
.tweet .mark{width:22px;height:22px;background:#4aa3d9;border-radius:4px;flex:none;margin-top:4px}
.tweet p{font-size:9.2px;line-height:14px;color:#6a6a6a}
.tweet p span{color:var(--link)}
.tweet p em{font-style:normal;color:#b8b8b8;display:block}
.photos{left:537px;top:823px;display:grid;grid-template-columns:repeat(4,45px);grid-template-rows:repeat(2,43px);gap:10px 11px}
.photos div{background:linear-gradient(180deg,#c9d3dc,#4f5d6c)}
.footer{left:0;top:957px;width:847px;height:192px;background:var(--footer)}
.footer h5{position:absolute;top:25px;font-size:12.5px;color:#fff;font-weight:400}
.footer .small{position:absolute;font-size:7.6px;line-height:11.6px;color:#8d8f90}
.portrait{left:101px;top:59px;width:95px;height:101px;border:3px solid #b5b5b5;background:linear-gradient(160deg,#d8d8d8,#6e6e6e)}
.role{left:205px;top:57px;font-size:11px;color:#e6e6e6}
.lang-select{left:571px;top:116px;width:165px;height:17px;background:#8b8d8e;color:#f2f2f2;font-size:7px;font-style:italic;display:flex;align-items:center;justify-content:space-between;padding:0 7px}
.bottom{left:0;top:1149px;width:847px;height:51px;background:var(--footer-bottom)}
.bottom .legal{left:106px;top:22px;font-size:9px;color:#a3a5a6}
.bottom .icons{left:627px;top:15px;display:flex;gap:5px;align-items:center}
.bottom .icons .badge{width:20px;height:18px;background:#e8e8e8;margin-right:12px}
.bottom .icons span{width:20px;height:20px;border-radius:50%;display:block}
</style>
</head>
<body>
<header class="abs topbar">
  <div class="abs rule"></div>
  <div class="abs email"><svg viewBox="0 0 11 9"><path d="M0 3L5.5 0 11 3V9H0Z M0 3L5.5 6 11 3" fill="none" stroke="#b9bcbe"/></svg>Email us at: email@example.com</div>
  <div class="abs social-top"><span></span><span></span><span></span><span></span><span></span></div>
  <div class="abs brand"><div class="name">Keystone Funding<i></i></div><div class="sub">A Ridgeline Capital Company</div></div>
  <nav class="abs nav"><a class="active">Home</a><a>About</a><a>Builders</a><a>Mortage Info</a><a>Approval</a><a>Blog</a><a>Contact</a></nav>
</header>

<section class="abs hero" role="img" aria-label="Smiling couple piggybacking on a lawn in front of a brick house">
  <div class="abs lawn"></div>
</section>
<div class="abs hero-box">
  <h1>Earning Your Business</h1>
  <p>The Marisol Brandt Team relies on strong systems to deliver on-time, done-right and friendly eperience</p>
</div>
<div class="abs cta"><span class="btn red">Start Here</span><span class="or">– Or –</span><span class="btn dark">Get to Know Us</span></div>

<h2 class="abs section-title" style="top:519px">Our Credentials</h2>
<article class="abs card" style="left:83px">
  <div class="band"><div class="icon"><svg width="20" height="18" viewBox="0 0 20 18"><rect x="1" y="1" width="18" height="12" fill="none" stroke="#fff" stroke-width="2"/><path d="M7 17h6M10 13v4" stroke="#fff" stroke-width="2"/></svg></div><h3>Awards</h3></div>
  <p>Lorem Ipsum is simply dummy text of the printing and typesetting industry. Lorem Ipsum has been the industry's standard dummy text ever since the 1500s, when an unknown printer took a galley of type and scrambled it to make a type specimen book. It has survived not only five centuries.</p>
</article>
<article class="abs card" style="left:433px">
  <div class="band"><div class="icon"><svg width="18" height="22" viewBox="0 0 18 22"><path d="M2 1h9l5 5v15H2Z" fill="none" stroke="#fff" stroke-width="2"/><path d="M5 11h8M5 15h8" stroke="#fff" stroke-width="2"/></svg></div><h3>Recognition</h3></div>
  <p>Lorem Ipsum is simply dummy text of the printing and typesetting industry. Lorem Ipsum has been the industry's standard dummy text ever since the 1500s, when an unknown printer took a galley of type and scrambled it to make a type specimen book. It has survived not only five centuries.</p>
</article>

<h2 class="abs section-title" style="top:734px">Engaged In our Community</h2>
<h4 class="abs col-label" style="left:85px;font-weight:400">From the Blog</h4>
<h4 class="abs col-label" style="left:324px;font-weight:400">Social News</h4>
<h4 class="abs col-label" style="left:535px;font-weight:400">In the Community</h4>

<div class="abs blog-icon"><svg width="18" height="16" viewBox="0 0 18 16"><path d="M2 14V9a7 7 0 0 1 14 0v5" fill="none" stroke="#fff" stroke-width="2"/><rect x="1" y="10" width="4" height="6" fill="#fff"/><rect x="13" y="10" width="4" height="6" fill="#fff"/></svg></div>
<div class="abs blog-date"><b>31</b><small>01,13</small></div>
<div class="abs blog-post">
  <h4>Contrary to popula beliefl orem the Ipsum is simply</h4>
  <p>Lorem Ipsum is dummy text the printing and typesetting instry. Ipsum has been.Lorem Ipsis sly</p>
  <a>Reda More ...</a>
</div>
<div class="abs dotted" style="left:85px;top:932px;width:213px"></div>

<div class="abs tweet" style="top:820px"><div class="mark"></div><p><span>@lena_hollis</span> Lorem Ipsum is the dummy text the printing typeset-ting instry Ipsum is has been.Lorem<em>3 days ago</em></p></div>
<div class="abs dotted" style="left:311px;top:885px;width:212px"></div>
<div class="abs tweet" style="top:898px"><div class="mark" style="background:#3b5b98"></div><p><span>@lena_hollis</span> Lorem Ipsum is the dummy text the printing typeset-<em>3 days ago</em></p></div>

<div class="abs photos" role="img" aria-label="Grid of eight community photos of the team"><div></div><div></div><div></div><div></div><div></div><div></div><div></div><div></div></div>

<footer class="abs footer">
  <h5 style="left:101px">About Marisol Brandt</h5>
  <h5 style="left:355px">Disclaimer</h5>
  <h5 style="left:571px">Language</h5>
  <div class="abs portrait" role="img" aria-label="Black and white portrait of Marisol Brandt"></div>
  <div class="abs role">Branch Manager</div>
  <div class="small" style="left:205px;top:78px">Office: 555.014.2200<br>Cell: 555.014.8830<br>mbrandt@keystonefunding.example<br>NMLS: 4821<br>2210 Meadow Square, Ste.140<br>Cedar Vale, TX 75099<br>Directions</div>
  <div class="small" style="left:355px;top:59px;width:170px">In accordance with Section 326 of the USA PATRIOT Act of 2001, Keystone Funding is required to obtain a copy of the documents used in identifying our new account custom-ers. This notice is being provided to you for adequate notice given under this act.</div>
  <div class="small" style="left:571px;top:59px;width:165px">Lorem Ipsum is simply dummy text of the printing and typesetting industry. Lorem Ipsum has been the industry's standard dummy text ever since the 1500s been the</div>
  <div class="abs lang-select">English<svg width="7" height="5" viewBox="0 0 7 5"><path d="M0 0h7L3.5 5Z" fill="#eee"/></svg></div>
</footer>
<div class="abs bottom">
  <div class="abs legal">Marisol Brandt • Legal</div>
  <div class="abs icons"><i class="badge"></i><span style="background:#5aa9cf"></span><span style="background:#4867a8"></span><span style="background:#d8661c"></span></div>
</div>
</body>
</html>
```